International Lifestyle Real Estate Brokerage Needs Eye Catching Website

We need a new website for a cutting edge / dynamic real estate startup, Palmcrest Homes, that will serve as a concierge brokerage to assist cold weather residents with the research, selection, financing and purchase of vacation / retirement properties in warm weather climates in the US and then globally. We will have personally vetted all properties to insure that our clients are only getting the best of the best with no hidden surprises.

** The website design will ultimately need to be coded into a wordpress theme.

We are not locked into any specific colour scheme but would prefer something warm vs cold as that is really the lifestyle we are selling. We like lots of white negative space and hope to allow high end photography to provide most of the pop in colour.

I have attached mock up wire frames to demonstrate desired functionality for three pages we need designed

1) Home Page
2) Market Profile (City overview and developments)
3) Community Profile Page (Individual development profile)

I have also included .ai file for the logo. Not locked into red.

Final design should communicate excitement, lifestyle while maintaining an air of professionalism and reliability. We have developed over 30 sites and have high expectations for the winning design.

Regards,
Dan

Target Market(s)

Canadian and Northern US residents looking to purchase vacation or retirement real estate in warmer climates, initially in the US, but eventually Internationally.

Industry/Entity Type

Real Estate

Contact Information for Business Card

Names for Business Cards

Dan Fairholt
604.555.2716
dan@palmcresthomes.ca

Coding

Coded - Design and coding required

Number of Pages Required

3 page

Font styles to use
Serif
Sans Serif

Requirements
Must have
• See wireframe documents uploaded.
• Site design will ultimately be coded into a child theme to function on a selected wordpress theme. If the designer has a Wordpres Theme in mind that would be compatible with the design we would appreciate that information.
Nice to have
• See wireframe documents uploaded. Prefer clean, modern site, white negative space, bold photography will add most of the colour and pop.
Should not have
• Anything cartoony or sophmoric.

```html
<!DOCTYPE html>
<html lang="en">
<head>
<meta charset="utf-8">
<title>Palmcrest Homes — Life Is Too Short To Be Cold</title>
<link rel="stylesheet" href="https://fonts.googleapis.com/css2?family=Oswald:wght@400;500&family=Montserrat:wght@400;600&family=Arimo:wght@400&display=swap">
<style>
:root{
  --red:#ec2f35;
  --navy:#343e4e;
  --ink:#1c2331;
  --light:#e8e8e8;
  --topbar:#dcdcdc;
  --footer:#2c2f33;
  --white:#ffffff;
  --muted:#6a6f78;
  --line:#b9bec6;
}
*{box-sizing:border-box;margin:0;padding:0}
html,body{width:1200px;height:3448px;overflow:hidden}
body{position:relative;background:var(--white);font-family:"Arimo",Arial,sans-serif;color:var(--ink)}
.section{position:absolute;left:0;width:1200px}
.abs{position:absolute}
.heading{font-family:"Oswald",sans-serif;font-weight:500;text-transform:uppercase;text-align:center;width:1200px;left:0;letter-spacing:1px}

/* top bar + nav */
.topbar{top:0;height:32px;background:var(--topbar)}
.utility{right:160px;top:8px;font-size:12px;color:var(--muted);display:flex;gap:14px}
.utility span.sep{color:#aaa}
.site-header{top:32px;height:69px;background:var(--white)}
.brand{left:161px;top:0;width:124px;height:101px;background:var(--red);display:flex;align-items:center;justify-content:center;text-align:center;color:var(--white);font-family:"Oswald",sans-serif;font-weight:500;font-size:15px;line-height:1.15;letter-spacing:1px;z-index:3}
.main-nav{left:521px;top:50px;display:flex;align-items:center;gap:22px;font-family:"Montserrat",sans-serif;font-size:12px;font-weight:600;z-index:3}
.main-nav .active{background:var(--red);color:var(--white);padding:7px 13px}
.btn-register{margin-left:28px;background:var(--navy);color:var(--white);padding:7px 34px;border:2px solid #222}

/* hero */
.hero{top:101px;height:501px;background:linear-gradient(180deg,#7a6a6c 0%,#4a4a52 35%,#2f3440 70%,#3d4150 100%)}
.hero-title{top:180px;font-size:44px;color:var(--white)}
.search{left:214px;top:267px;width:772px;height:46px;background:var(--white);border-radius:3px;display:flex;align-items:center;padding:0 28px;font-size:13px;color:#9aa0a8;justify-content:space-between}

/* services */
.services{top:602px;height:660px;background:var(--light)}
.services .heading{top:62px;font-size:44px}
.service{top:191px;width:200px}
.service .icon{width:90px;height:90px;background:var(--navy);border-radius:6px;display:flex;align-items:center;justify-content:center}
.service .icon.hot{background:var(--red)}
.service .label{position:absolute;left:98px;top:28px;font-size:13px;color:#444;line-height:1.3;text-transform:uppercase}
.service p{margin-top:18px;font-size:11px;line-height:1.5;color:var(--muted)}
.service .more{display:inline-block;margin-top:14px;background:var(--navy);color:var(--white);font-family:"Montserrat",sans-serif;font-size:9px;font-weight:600;padding:8px 14px}
.service .more.hot{background:var(--red)}
.cta{left:467px;top:513px;width:266px;height:51px;border:2px solid var(--red);display:flex;align-items:center;justify-content:center;font-family:"Montserrat",sans-serif;font-size:19px;color:var(--ink)}

/* developments */
.developments{top:1262px;height:499px;background:var(--navy)}
.developments .heading{top:60px;font-size:44px;color:var(--white)}
.dev-photo{top:170px;width:377px;height:267px;border:3px solid var(--red)}
.arrow{width:40px;height:40px;border:2px solid rgba(255,255,255,.7);border-radius:50%;display:flex;align-items:center;justify-content:center;top:281px}

/* markets */
.markets{top:1761px;height:754px;background:var(--light)}
.markets .heading{top:62px;font-size:44px}
.tab{top:193px;height:44px;display:flex;align-items:center;justify-content:center;font-family:"Montserrat",sans-serif;font-size:12px;font-weight:600;border:2px solid #8d939c;background:#e0e3e7}
.tab.active{background:var(--red);color:var(--white);border-color:var(--red)}
.market-card{width:269px;height:150px;background:var(--white);box-shadow:0 1px 3px rgba(0,0,0,.25);border-radius:3px;overflow:hidden}
.market-card .photo{height:110px}
.market-card .name{text-align:center;font-family:"Montserrat",sans-serif;font-weight:600;font-size:13px;padding-top:11px;letter-spacing:1px}
.commitment{left:768px;top:490px;width:270px}
.commitment h3{font-family:"Montserrat",sans-serif;font-size:13px;font-weight:600;letter-spacing:.5px}
.commitment p{margin-top:14px;font-size:11px;line-height:1.55;color:var(--muted);width:210px}
.commitment .more{display:inline-block;margin-top:22px;background:var(--red);color:var(--white);font-family:"Montserrat",sans-serif;font-size:9px;font-weight:600;padding:8px 20px}

/* blog */
.blog{top:2515px;height:421px;background:var(--white)}
.blog .heading{top:58px;font-size:30px}
.post{width:400px;height:62px}
.post .thumb{position:absolute;left:0;top:0;width:60px;height:62px}
.post h4{position:absolute;left:74px;top:0;font-family:"Montserrat",sans-serif;font-size:12px;font-weight:600;letter-spacing:.3px}
.post p{position:absolute;left:74px;top:20px;width:290px;font-size:11px;line-height:1.5;color:var(--muted)}

/* newsletter */
.newsletter{top:2936px;height:283px;background:var(--navy)}
.newsletter .heading{top:70px;font-size:30px;color:var(--white)}
.subscribe{left:315px;top:147px;width:577px;height:44px;background:var(--white);border-radius:22px;overflow:hidden}
.subscribe .field{position:absolute;left:26px;top:14px;font-size:11px;color:#9aa0a8}
.subscribe .submit{position:absolute;right:0;top:0;width:126px;height:44px;background:var(--red);border-radius:22px;color:var(--white);font-family:"Montserrat",sans-serif;font-weight:600;font-size:14px;display:flex;align-items:center;justify-content:center}

/* footer */
.site-footer{top:3219px;height:229px;background:var(--footer)}
.site-footer .heading{top:48px;font-size:22px;color:var(--white)}
.social{top:104px;left:508px;display:flex;gap:18px}
.social span{width:32px;height:32px;border-radius:50%;background:#5b6f96}
.social span:nth-child(3),.social span:nth-child(4){background:#d9555a}
.social span:nth-child(2){background:#6b9dc8}
.footer-links{top:178px;left:0;width:1200px;display:flex;justify-content:center;gap:18px;font-size:11px;color:#e6e6e6}
.footer-links .sep{color:#888}
</style>
</head>
<body>

<div class="section topbar">
  <div class="abs utility"><span>Saved</span><span class="sep">|</span><span>About</span><span class="sep">|</span><span>Contact</span><span class="sep">|</span><span>Login</span></div>
</div>

<header class="section site-header"></header>
<div class="abs brand">PALMCREST<br>HOMES</div>
<nav class="abs main-nav">
  <span class="active">HOME</span><span>SEARCH</span><span>OUR PROCESS</span><span>RESOURCES</span>
  <span class="btn-register">REGISTER</span>
</nav>

<section class="section hero" role="img" aria-label="Aerial photograph of a city skyline at dusk with a river winding through">
  <h1 class="abs heading hero-title">Life Is Too Short To Be Cold</h1>
  <div class="abs search"><span>Where Do You Want to Play in The Sunshine ?</span>
    <svg width="24" height="24" viewBox="0 0 24 24" fill="none" stroke="#ec2f35" stroke-width="2.6"><circle cx="10" cy="10" r="7"/><line x1="15" y1="15" x2="22" y2="22"/></svg>
  </div>
</section>

<section class="section services">
  <h2 class="abs heading">We’re Service Provided</h2>

  <div class="abs service" style="left:161px">
    <div class="icon"><svg width="40" height="40" viewBox="0 0 40 40" fill="none" stroke="#fff" stroke-width="2.5"><polyline points="4,4 4,36 36,36"/><polyline points="9,28 17,18 23,24 33,12"/></svg></div>
    <div class="label">Dynamic<br>Real Estate</div>
    <p>Our team vets every listing in person so you buy with full confidence. We guide research, financing and closing from start to finish with care.</p>
    <span class="more">LEARN MORE</span>
  </div>
  <div class="abs service" style="left:386px">
    <div class="icon"><svg width="40" height="40" viewBox="0 0 40 40" fill="none" stroke="#fff" stroke-width="2.5"><path d="M18 8a13 13 0 1 0 13 13H18z"/><path d="M22 4a13 13 0 0 1 13 13H22z"/></svg></div>
    <div class="label">Dynamic<br>Real Estate</div>
    <p>Our team vets every listing in person so you buy with full confidence. We guide research, financing and closing from start to finish with care.</p>
    <span class="more">LEARN MORE</span>
  </div>
  <div class="abs service" style="left:611px">
    <div class="icon"><svg width="42" height="40" viewBox="0 0 42 40" fill="none" stroke="#fff" stroke-width="2.5"><path d="M12 30H9a7 7 0 0 1 0-14 11 11 0 0 1 21-2 8 8 0 0 1 3 16h-3"/><line x1="21" y1="36" x2="21" y2="20"/><polyline points="15,25 21,19 27,25"/></svg></div>
    <div class="label">Dynamic<br>Real Estate</div>
    <p>Our team vets every listing in person so you buy with full confidence. We guide research, financing and closing from start to finish with care.</p>
    <span class="more">LEARN MORE</span>
  </div>
  <div class="abs service" style="left:837px">
    <div class="icon hot"><svg width="40" height="40" viewBox="0 0 40 40" fill="none" stroke="#fff" stroke-width="2.5"><path d="M30 22v12H6V10h12"/><polyline points="24,5 35,5 35,16"/><line x1="35" y1="5" x2="18" y2="22"/></svg></div>
    <div class="label">Dynamic<br>Real Estate</div>
    <p>Our team vets every listing in person so you buy with full confidence. We guide research, financing and closing from start to finish with care.</p>
    <span class="more hot">LEARN MORE</span>
  </div>

  <div class="abs cta">REGISTER CTA</div>
</section>

<section class="section developments">
  <h2 class="abs heading">Featured Developments</h2>
  <div class="abs arrow" style="left:159px"><svg width="14" height="14" viewBox="0 0 14 14" fill="none" stroke="#fff" stroke-width="2"><polyline points="9,2 4,7 9,12"/></svg></div>
  <div class="abs dev-photo" style="left:214px;background:linear-gradient(135deg,#8c8f95,#4a3a34 55%,#6e7077)" role="img" aria-label="Photograph of downtown high-rise towers above a busy street"></div>
  <div class="abs dev-photo" style="left:609px;background:linear-gradient(180deg,#8fc3ea 0%,#cfe0ec 45%,#8e96a0 75%,#5f6670 100%)" role="img" aria-label="Photograph of a city skyline behind a large highway interchange"></div>
  <div class="abs arrow" style="left:998px"><svg width="14" height="14" viewBox="0 0 14 14" fill="none" stroke="#fff" stroke-width="2"><polyline points="5,2 10,7 5,12"/></svg></div>
</section>

<section class="section markets">
  <h2 class="abs heading">Featured Markets</h2>
  <div class="abs tab active" style="left:313px;width:124px">UNITED STATES</div>
  <div class="abs tab" style="left:536px;width:128px">MEXICO</div>
  <div class="abs tab" style="left:761px;width:126px">SOUTH AMERICA</div>

  <div class="abs market-card" style="left:161px;top:313px">
    <div class="photo" style="background:linear-gradient(180deg,#a9cdee,#8c9aa5 60%,#2f7d86)" role="img" aria-label="Photograph of the Orlando skyline across a lake"></div>
    <div class="name">ORLANDO</div>
  </div>
  <div class="abs market-card" style="left:462px;top:313px">
    <div class="photo" style="background:linear-gradient(180deg,#1f7fd6,#0e5fb8 60%,#c8664f)" role="img" aria-label="Photograph of blue ocean seen from a seaside building in Naples"></div>
    <div class="name">NAPLES</div>
  </div>
  <div class="abs market-card" style="left:768px;top:313px">
    <div class="photo" style="background:linear-gradient(135deg,#f2f2f2,#c9ccd0 60%,#7c7f86)" role="img" aria-label="Photograph of a smiling real estate team in Fort Myers"></div>
    <div class="name">FORT MEYERS</div>
  </div>
  <div class="abs market-card" style="left:161px;top:494px">
    <div class="photo" style="background:linear-gradient(180deg,#7fa9b8,#2e8f93 55%,#e8f2f2)" role="img" aria-label="Photograph of turquoise water and surf at Clearwater beach"></div>
    <div class="name">CLEARWATER</div>
  </div>
  <div class="abs market-card" style="left:462px;top:494px">
    <div class="photo" style="background:linear-gradient(180deg,#9fc2e6,#b4bcc4 55%,#5b6b55)" role="img" aria-label="Photograph of the Asheville city skyline"></div>
    <div class="name">ASHEVILLE</div>
  </div>

  <div class="abs commitment">
    <h3>OUR COMMITMENT</h3>
    <p>Every home we show has been personally vetted by our team. No hidden surprises, only the best.</p>
    <span class="more">VIEW MORE</span>
  </div>
</section>

<section class="section blog">
  <h2 class="abs heading">Recent Blog Posts</h2>
  <div class="abs post" style="left:161px;top:161px">
    <div class="thumb" style="background:linear-gradient(180deg,#8fb6d4,#c9a48c)" role="img" aria-label="Author portrait"></div>
    <h4>DYNAMIC REAL ESTATE BLOG</h4>
    <p>Tips for buying a warm weather home, from choosing a market to closing day with ease.</p>
  </div>
  <div class="abs post" style="left:669px;top:161px">
    <div class="thumb" style="background:linear-gradient(135deg,#e6e1da,#c97f5b)" role="img" aria-label="Photograph of hands holding a small model house"></div>
    <h4>DYNAMIC REAL ESTATE BLOG</h4>
    <p>Tips for buying a warm weather home, from choosing a market to closing day with ease.</p>
  </div>
  <div class="abs post" style="left:161px;top:260px">
    <div class="thumb" style="background:linear-gradient(180deg,#a9c2d6,#6b6a5e 60%,#4d6b3e)" role="img" aria-label="Photograph of a suburban house"></div>
    <h4>DYNAMIC REAL ESTATE BLOG</h4>
    <p>Tips for buying a warm weather home, from choosing a market to closing day with ease.</p>
  </div>
  <div class="abs post" style="left:669px;top:260px">
    <div class="thumb" style="background:linear-gradient(135deg,#2d3a66,#b07a5e)" role="img" aria-label="Author portrait"></div>
    <h4>DYNAMIC REAL ESTATE BLOG</h4>
    <p>Tips for buying a warm weather home, from choosing a market to closing day with ease.</p>
  </div>
</section>

<section class="section newsletter">
  <h2 class="abs heading">Subscribe Our Newsletter</h2>
  <div class="abs subscribe">
    <span class="field">your email address</span>
    <span class="submit">SUBMIT</span>
  </div>
</section>

<footer class="section site-footer">
  <h2 class="abs heading">Say Hi, Get In Touch</h2>
  <div class="abs social" aria-label="Social links"><span></span><span></span><span></span><span></span></div>
  <nav class="abs footer-links">
    <span>Home</span><span class="sep">|</span><span>About</span><span class="sep">|</span><span>Contact</span><span class="sep">|</span><span>Login</span><span class="sep">|</span><span>Saved</span><span class="sep">|</span><span>Search</span><span class="sep">|</span><span>Our Process</span><span class="sep">|</span><span>Resources</span>
  </nav>
</footer>

</body>
</html>
```